Wine gifting platform needs redeem/decline page

Tavirel is a wine gifting platform. Users can send wine gifts to one or many people, the recipients will then receive an email with instructions on how to redeem their wine.

This is what we need: After clicking the link in the email they will be taken to the redeem/decline page/flow where they will choose their preferred wine and enter their shipping address. I have uploaded videos of both the decline and the redeem flows.

- All existing form fields, informational text, and error messages needs to be incorporated into the new design but otherwise you have creative freedom on presentation.
- We have four gift tiers: Silver, Gold, Platinum, and Diamond. We would like the redemption page to highlight this with different colors (or something else!) that's glanceable. I have attached screenshots to highlight these.
- Our target audience is professional and corporate but we want the redemption process to feel elegant and sleek. We want it to feel like a premium experience just like the wine they'll receive.

I would prefer Sketch files over Photoshop.

Target Market(s)

Professional, corporate

Number of Pages Required

3 page

Requirements
Must have
• All fields, all 3 steps of the wizard, information, and error messages/styles in the flow videos (attached)

```html
<!DOCTYPE html>
<html lang="en">
<head>
<meta charset="utf-8">
<title>Tavirel – Enter Your Address</title>
<link rel="stylesheet" href="https://fonts.googleapis.com/css2?family=Poppins:wght@400;600&family=Fira+Sans+Condensed:wght@500;600&display=swap">
<style>
  :root {
    --brand: #0a43b0;
    --page: #eff3fa;
    --card: #ffffff;
    --ink: #1d1d1f;
    --muted-ring: #d7e0f1;
    --field-border: #bccae6;
    --box-border: #c9d4ea;
    --rule: #dfe3ec;
  }
  * { box-sizing: border-box; margin: 0; padding: 0; }
  html, body { width: 1200px; height: 986px; overflow: hidden; }
  body {
    position: relative;
    background: var(--page);
    font-family: "Poppins", sans-serif;
    color: var(--ink);
  }
  .site-header {
    position: absolute; left: 0; top: 0; width: 1200px; height: 82.5px;
    background: var(--brand);
    display: flex; align-items: center; justify-content: center;
  }
  .brand-name {
    color: #fff; font-family: "Poppins", sans-serif; font-weight: 600;
    font-size: 38px; letter-spacing: 0.5px;
  }

  .step-circle {
    position: absolute; width: 60px; height: 60px; border-radius: 50%;
    background: var(--muted-ring);
    display: flex; align-items: center; justify-content: center;
  }
  .step-circle span {
    width: 46px; height: 46px; border-radius: 50%; background: #fff;
    display: flex; align-items: center; justify-content: center;
    font-family: "Fira Sans Condensed", sans-serif; font-weight: 600; font-size: 28px;
  }
  .step-label {
    position: absolute; width: 200px; text-align: center; top: 199px;
    font-family: "Fira Sans Condensed", sans-serif; font-weight: 600; font-size: 18.5px;
  }
  .is-active { color: var(--brand); }
  .step-arrow { position: absolute; top: 152px; }

  .form-card {
    position: absolute; left: 60px; top: 279px; width: 1080px; height: 645px;
    background: var(--card); border-radius: 30px;
  }
  .error-summary {
    position: absolute; left: 75px; top: 295.5px; width: 293px; height: 327px;
    background: var(--page); border: 1px solid var(--box-border); border-radius: 14px;
    list-style: none;
  }
  .error-summary li {
    position: absolute; left: 37px; width: 250px;
    font-size: 13.5px; line-height: 22.5px;
  }
  .error-summary li::before {
    content: "*"; position: absolute; left: -19px; top: 1px;
    color: var(--brand); font-weight: 600; font-size: 15px;
  }

  .field-label {
    position: absolute; font-size: 13.5px; line-height: 18px;
  }
  .req { color: var(--brand); margin-left: 3px; position: relative; top: -3px; }
  .field-input {
    position: absolute; height: 39px; border: 1px solid var(--field-border);
    border-radius: 7px; background: #fff;
  }
  .rule { position: absolute; left: 409px; width: 705px; height: 1px; background: var(--rule); }

  .check-row {
    position: absolute; left: 416px; display: flex; align-items: center;
    font-size: 13.5px; line-height: 18px;
  }
  .check-box {
    width: 13px; height: 13px; border: 1.5px solid #555; border-radius: 2px;
    margin-right: 11px; flex: none;
  }
  .text-link { color: var(--brand); }

  .btn {
    position: absolute; top: 843px; height: 35px; border-radius: 9px;
    display: flex; align-items: center; justify-content: center; gap: 9px;
    font-family: "Fira Sans Condensed", sans-serif; font-weight: 500; font-size: 17px;
  }
  .btn-back { left: 925.5px; width: 91px; border: 1px solid var(--brand); color: var(--brand); background: #fff; }
  .btn-next { left: 1026px; width: 89px; background: var(--brand); color: #fff; }
</style>
</head>
<body>
  <header class="site-header"><span class="brand-name">Tavirel</span></header>

  <div class="step-circle" style="left:364.5px;top:129px"><span>1</span></div>
  <div class="step-circle" style="left:570px;top:129px"><span class="is-active">2</span></div>
  <div class="step-circle" style="left:768px;top:129px"><span>3</span></div>

  <svg class="step-arrow" style="left:450px" width="104" height="14" viewBox="0 0 104 14">
    <line x1="0" y1="7" x2="90" y2="7" stroke="#0a43b0" stroke-width="1.5" stroke-dasharray="1.5 2.5"/>
    <path d="M90 0 L103 7 L90 14 Z" fill="#0a43b0"/>
  </svg>
  <svg class="step-arrow" style="left:648.5px" width="104" height="14" viewBox="0 0 104 14">
    <line x1="0" y1="7" x2="90" y2="7" stroke="#0a43b0" stroke-width="1.5" stroke-dasharray="1.5 2.5"/>
    <path d="M90 0 L103 7 L90 14 Z" fill="#0a43b0"/>
  </svg>

  <div class="step-label" style="left:297px">Choose Your Gift</div>
  <div class="step-label is-active" style="left:500px">Enter Your Address</div>
  <div class="step-label" style="left:700px">Confirm</div>

  <main class="form-card"></main>

  <ul class="error-summary">
    <li style="top:26px">Phone # is required.</li>
    <li style="top:55px">Address is required.</li>
    <li style="top:87px">City is required.</li>
    <li style="top:117px">State is required.</li>
    <li style="top:150px">Postal Code is required.</li>
    <li style="top:187px">You must confirm that you are of legal drinking age.</li>
    <li style="top:243px">You must agree to the Privacy Policy and Terms of Services.</li>
  </ul>

  <label class="field-label" style="left:410px;top:323px">First Name</label>
  <div class="field-input" style="left:407px;top:348px;width:346px"></div>
  <label class="field-label" style="left:773px;top:323px">Last Name</label>
  <div class="field-input" style="left:769.5px;top:348px;width:346px"></div>

  <label class="field-label" style="left:410px;top:409px">Email Address</label>
  <div class="field-input" style="left:407px;top:433.5px;width:346px"></div>
  <label class="field-label" style="left:773px;top:409px">Phone #<span class="req">*</span></label>
  <div class="field-input" style="left:769.5px;top:433.5px;width:346px"></div>

  <label class="field-label" style="left:410px;top:495px">Address<span class="req">*</span></label>
  <div class="field-input" style="left:407px;top:520px;width:346px"></div>
  <label class="field-label" style="left:773px;top:495px">Address(Apt/Floor/Suite)</label>
  <div class="field-input" style="left:769.5px;top:520px;width:346px"></div>

  <label class="field-label" style="left:410px;top:585px">City<span class="req">*</span></label>
  <div class="field-input" style="left:407px;top:610px;width:226px"></div>
  <label class="field-label" style="left:650px;top:585px">State<span class="req">*</span></label>
  <div class="field-input" style="left:647px;top:610px;width:226px"></div>
  <label class="field-label" style="left:890px;top:585px">Postal Code<span class="req">*</span></label>
  <div class="field-input" style="left:887px;top:610px;width:226px"></div>

  <div class="rule" style="top:684px"></div>
  <div class="check-row" style="top:701px"><span class="check-box"></span>I want to subscribe to emails from Tavirel to learn how to quickly and easily send wine gifts.</div>
  <div class="rule" style="top:738px"></div>
  <div class="check-row" style="top:755px"><span class="check-box"></span>I confirm that I am of legal drinking age in my state.<span class="req">*</span></div>
  <div class="check-row" style="top:784.5px"><span class="check-box"></span>I agree to the&nbsp;<span class="text-link">Privacy Policy</span>&nbsp;and&nbsp;<span class="text-link">Terms of Services.</span><span class="req">*</span></div>
  <div class="rule" style="top:820.5px"></div>

  <a class="btn btn-back">
    <svg width="26" height="12" viewBox="0 0 26 12"><path d="M25 6 H2 M7 1 L1.5 6 L7 11" fill="none" stroke="#0a43b0" stroke-width="1.6"/></svg>
    Back
  </a>
  <a class="btn btn-next">
    Next
    <svg width="26" height="12" viewBox="0 0 26 12"><path d="M1 6 H24 M19 1 L24.5 6 L19 11" fill="none" stroke="#fff" stroke-width="1.6"/></svg>
  </a>
</body>
</html>
```